Brixel Solutions Website Creation

Create a business website for custom flexible packaging and MDF products. The www.Olvane.com website is generic page that you can use to create a similar home page for my business.
Specifically: https://www.olvane.com/packaging/
https://www.olvane.com/product/mdf-panels/
Domain is Brix-El.com
I would like the page to have a more packaging related look than the MDF/wood.

```html
<!DOCTYPE html>
<html lang="en">
<head>
<meta charset="utf-8">
<title>Brixel Solutions — Custom Flexible Packaging</title>
<link href="https://fonts.googleapis.com/css2?family=Inter:wght@400;500;600;700;800&family=Inter+Tight:wght@600;700;800&display=swap" rel="stylesheet">
<style>
:root{
  --stage:#b3b3b3;
  --navy:#0b1a2e;
  --navy-2:#12284b;
  --ink:#0f1a33;
  --blue:#1ea7f5;
  --blue-deep:#1a86d6;
  --muted:#5b6577;
  --line:#e6ebf2;
  --pale:#f4f7fb;
  --white:#ffffff;
}
*{box-sizing:border-box;margin:0;padding:0}
html,body{width:1200px;height:2733px;overflow:hidden}
body{background:var(--stage);font-family:"Inter",sans-serif;color:var(--ink)}
.page{position:absolute;left:81px;top:81px;width:1037px;height:2573px;background:var(--white);box-shadow:0 10px 30px rgba(0,0,0,.25);overflow:hidden}
section,header,footer{position:absolute;left:0;width:100%}
.abs{position:absolute}
.eyebrow{font-size:7px;font-weight:800;letter-spacing:1px;color:var(--blue);text-transform:uppercase}
.h2{font-family:"Inter Tight",sans-serif;font-weight:700;font-size:23px;line-height:25.5px;letter-spacing:-.6px;color:var(--ink)}
.dot{position:absolute;width:64px;height:64px;border-radius:50%;background:var(--blue)}
.body-s{font-size:9.5px;line-height:15.5px;color:var(--muted)}

/* hero */
.hero{top:0;height:576px;background:var(--navy)}
.brand{position:absolute;left:16px;top:22px;display:flex;align-items:center;gap:8px}
.brand-mark{width:14px;height:14px;border-radius:50%;background:var(--blue)}
.brand-name{font-size:22px;font-weight:500;color:var(--white);letter-spacing:-.4px}
.nav{position:absolute;right:16px;top:17px;display:flex;align-items:center;gap:28px}
.nav a{font-size:10px;font-weight:600;color:var(--white);text-decoration:none}
.nav a.active{color:var(--blue)}
.nav .btn-quote{background:var(--blue);color:var(--white);padding:7px 12px;border-radius:14px;margin-left:0}
.hero-eyebrow{left:41px;top:163px;font-size:13px;font-weight:500;color:var(--blue);letter-spacing:.2px}
.hero h1{position:absolute;left:40px;top:186px;width:500px;font-family:"Inter",sans-serif;font-weight:700;font-size:42px;line-height:50px;letter-spacing:-.3px;color:var(--white)}
.hero-lead{left:42px;top:348px;width:410px;font-size:13px;line-height:19.5px;color:#dfe7f2}
.hero-ctas{left:42px;top:432px;display:flex;gap:8px}
.btn{display:inline-block;font-size:10px;font-weight:600;border-radius:13px;padding:7px 12px;text-decoration:none}
.btn-blue{background:var(--blue);color:var(--white)}
.btn-light{background:var(--white);color:var(--blue)}
.hero-ring{left:535px;top:70px;width:520px;height:520px;border-radius:50%;background:radial-gradient(circle at 40% 45%,#135a93 0%,#0f3d6a 45%,rgba(11,26,46,0) 70%)}
.hero-products{left:570px;top:100px;width:430px;height:410px;border-radius:14px;background:linear-gradient(160deg,#f1f3f6 0%,#d9dee5 50%,#2c5ec9 88%,#c78a45 100%)}

/* intro */
.intro{top:576px;height:572px;background:var(--white)}
.intro .dot.a{left:126px;top:77px}
.intro .eyebrow.a{left:200px;top:53px}
.intro .h2.a{left:200px;top:68px;width:270px}
.intro .body-s.a{left:523px;top:65px;width:300px}
.intro .dot.b{left:126px;top:276px}
.intro .eyebrow.b{left:200px;top:262px}
.intro .h2.b{left:200px;top:278px;width:340px}
.sol-card{position:absolute;top:349px;width:203px;height:170px;border-radius:10px;background:var(--white);box-shadow:0 6px 22px rgba(15,26,51,.08);padding:18px}
.sol-card.dark{background:var(--ink)}
.sol-icon{width:30px;height:30px;border-radius:8px;background:#eef6fd;display:flex;align-items:center;justify-content:center}
.sol-card.dark .sol-icon{background:var(--white)}
.sol-card h3{margin-top:16px;font-size:12px;font-weight:700;color:var(--ink)}
.sol-card.dark h3{color:var(--white)}
.sol-card p{margin-top:10px;font-size:8.5px;line-height:14px;color:var(--muted)}
.sol-card.dark p{color:#d5dbe6}

/* categories */
.cats{top:1148px;height:337px;background:linear-gradient(135deg,#0e2343 0%,#132e57 100%)}
.cats .dot{left:126px;top:77px}
.cats .eyebrow{left:200px;top:57px}
.cats .h2{left:200px;top:72px;width:220px;color:var(--white)}
.cats .lead{left:200px;top:164px;width:240px;font-size:9.5px;line-height:15.5px;color:#d5dbe6}
.cats .btn-light{position:absolute;left:200px;top:202px;padding:8px 13px;font-size:9px;box-shadow:0 0 18px rgba(30,167,245,.45)}
.cat-card{position:absolute;width:181px;border-radius:9px;background:rgba(255,255,255,.07);border:1px solid rgba(255,255,255,.12);padding:15px}
.cat-card h3{font-size:12px;font-weight:700;color:var(--white)}
.cat-card p{margin-top:9px;font-size:8.5px;line-height:14px;color:#cfd7e4}

/* serve */
.serve{top:1485px;height:325px;background:var(--white);text-align:center}
.serve .dot{left:486px;top:50px}
.serve .eyebrow{left:0;width:100%;top:130px}
.serve .h2{left:0;width:100%;top:146px}
.pills{position:absolute;left:200px;top:219px;width:638px;display:flex;gap:11px}
.pill{flex:1;height:53px;border-radius:8px;background:var(--white);box-shadow:0 4px 16px rgba(15,26,51,.08);display:flex;align-items:center;justify-content:center;font-size:9px;font-weight:700;color:var(--ink);line-height:14px;padding:0 10px}

/* mdf */
.mdf{top:1810px;height:304px;background:var(--pale)}
.mdf-photo{left:200px;top:54px;width:303px;height:194px;border-radius:10px;background:linear-gradient(90deg,#c9946a 0%,#dcae88 50%,#be875c 100%)}
.mdf .dot{left:459px;top:67px;border:6px solid var(--white);width:72px;height:72px}
.mdf .eyebrow{left:536px;top:57px}
.mdf .h2{left:536px;top:72px;width:300px}
.mdf .body-s{left:536px;top:130px;width:300px}
.ticks{position:absolute;left:536px;top:191px;list-style:none}
.ticks li{display:flex;align-items:center;gap:8px;font-size:8.5px;font-weight:700;color:var(--ink);height:20.5px}

/* cta */
.cta{top:2114px;height:108px;background:var(--blue)}
.cta h2{position:absolute;left:200px;top:34px;font-family:"Inter Tight",sans-serif;font-size:23px;font-weight:700;letter-spacing:-.6px;color:var(--white)}
.cta p{position:absolute;left:200px;top:68px;font-size:9.5px;color:#eaf6ff}
.cta a{position:absolute;left:768px;top:48px;font-size:9px;font-weight:700;color:var(--white);text-decoration:none}

/* contact */
.contact{top:2222px;height:287px;background:var(--white)}
.contact .dot{left:126px;top:70px}
.contact .eyebrow{left:200px;top:55px}
.contact .h2{left:200px;top:70px;width:240px}
.contact .details{left:200px;top:140px;font-size:9.5px;line-height:15.5px;color:var(--muted)}
.field{position:absolute;height:30px;border:1px solid var(--line);border-radius:6px;background:var(--white);font-size:8.5px;color:#6f7888;padding:0 9px;display:flex;align-items:center}
.field.select{justify-content:space-between;color:var(--ink)}
.field.area{height:70px;align-items:flex-start;padding-top:11px}
.submit{position:absolute;left:475px;top:212px;background:var(--blue);color:var(--white);font-size:7.5px;font-weight:700;padding:8px 13px;border-radius:12px;box-shadow:0 4px 12px rgba(30,167,245,.4)}

/* footer */
footer{top:2509px;height:64px;border-top:1px solid var(--line);background:var(--white)}
.foot-brand{position:absolute;left:200px;top:20px;display:flex;align-items:center;gap:6px}
.foot-brand .brand-mark{width:10px;height:10px}
.foot-brand span{font-size:13px;font-weight:500;color:var(--ink)}
.foot-copy{position:absolute;right:199px;top:30px;font-size:8.5px;color:var(--muted)}
</style>
</head>
<body>
<div class="page">

  <header class="hero">
    <div class="brand"><span class="brand-mark"></span><span class="brand-name">Brixel Solutions</span></div>
    <nav class="nav">
      <a class="active" href="#">Home</a>
      <a href="#">Solution</a>
      <a href="#">Products</a>
      <a href="#">Industries</a>
      <a href="#">MDF</a>
      <a class="btn-quote" href="#">Request Quote</a>
    </nav>
    <div class="abs hero-ring"></div>
    <div class="abs hero-products" role="img" aria-label="Packaging products: stretch film rolls, stand-up pouches, spray bottles, droppers and a blue film roll"></div>
    <p class="abs hero-eyebrow">A GLOBAL TRADING PARTNER YOU CAN TRUST</p>
    <h1>Custom Flexible Packaging Built Around Your Product.</h1>
    <p class="abs hero-lead">Brixel Solutions supplies pouches, films, bags, bottles, stretch wrap, safety supplies, strapping and MDF products for growing brands, distributors and manufacturers.</p>
    <div class="abs hero-ctas">
      <a class="btn btn-blue" href="#">Request a Quote</a>
      <a class="btn btn-light" href="#">Explore Products</a>
    </div>
  </header>

  <section class="intro">
    <span class="dot a"></span>
    <p class="abs eyebrow a">Packaging-first website concept</p>
    <h2 class="abs h2 a">One supply partner for packaging, protection and custom product needs.</h2>
    <p class="abs body-s a">From roll stock films and stand-up pouches to clamshells, shrink bags, bottles, sprayers, stretch film and corrugated products, Brixel helps simplify sourcing while keeping quality and consistency at the center.</p>

    <span class="dot b"></span>
    <p class="abs eyebrow b">Core solutions</p>
    <h2 class="abs h2 b">Packaging solutions designed for performance.</h2>

    <div class="sol-card dark" style="left:200px">
      <div class="sol-icon"><svg width="18" height="18" viewBox="0 0 18 18"><rect x="2" y="2" width="14" height="14" rx="4" fill="none" stroke="#1ea7f5" stroke-width="1.6"/></svg></div>
      <h3>Flexible Packaging</h3>
      <p>Vacuum pouches, stand-up pouches, custom pouches and bags, roll stock films, shrink films, fruit pouches and agriculture films.</p>
    </div>
    <div class="sol-card" style="left:418px">
      <div class="sol-icon"><svg width="18" height="18" viewBox="0 0 18 18"><circle cx="9" cy="9" r="6" fill="#1ea7f5"/><circle cx="9" cy="9" r="3" fill="#fff"/></svg></div>
      <h3>Stretch Film</h3>
      <p>Machine film, hand film, coreless hand film, vented films and banding film for warehouse, logistics and manufacturing use.</p>
    </div>
    <div class="sol-card" style="left:635px">
      <div class="sol-icon"><svg width="18" height="18" viewBox="0 0 18 18"><path d="M9 2l6.5 3.7v6.6L9 16l-6.5-3.7V5.7z" fill="#1ea7f5"/></svg></div>
      <h3>Other Packaging</h3>
      <p>Corrugated boxes, rigid setup boxes, folding cartons, V-board, corner board, bottles, closures, caps, lids, sprayers and pumps.</p>
    </div>
  </section>

  <section class="cats">
    <span class="dot"></span>
    <p class="abs eyebrow">Product categories</p>
    <h2 class="abs h2">From shelf-ready pouches to industrial films.</h2>
    <p class="abs lead">Build a custom packaging mix for food, agriculture, retail, industrial, fulfillment and private-label needs.</p>
    <a class="btn btn-light" href="#">Talk to Brixel</a>

    <div class="cat-card" style="left:466px;top:51px;height:118px">
      <h3>Flexible Packaging</h3>
      <p>Vacuum pouches, stand-up pouches, custom pouches &amp; bags, roll stock films, shrink films, shrink bags, fruit pouches.</p>
    </div>
    <div class="cat-card" style="left:657px;top:51px;height:118px">
      <h3>Poly &amp; Bottles</h3>
      <p>Mattress films, box liners, tote liners, poly bags, plastic &amp; glass bottles, droppers, caps and lids.</p>
    </div>
    <div class="cat-card" style="left:466px;top:180px;height:104px">
      <h3>Stretch &amp; Banding</h3>
      <p>Machine film, hand film, vented films, banding film, polypropylene, polyester and steel strapping.</p>
    </div>
    <div class="cat-card" style="left:657px;top:180px;height:104px">
      <h3>Safety Supplies</h3>
      <p>Hand protection, protective garments, eye protection, head protection, face masks and sleeves.</p>
    </div>
  </section>

  <section class="serve">
    <span class="dot"></span>
    <p class="abs eyebrow">Who we serve</p>
    <h2 class="abs h2">Reliable sourcing for brands that need<br>packaging to work.</h2>
    <div class="pills">
      <div class="pill">Food &amp; Beverage</div>
      <div class="pill">Agriculture</div>
      <div class="pill">Retail &amp; E-commerce</div>
      <div class="pill">Manufacturing</div>
      <div class="pill">Warehousing</div>
      <div class="pill">Private Label</div>
    </div>
  </section>

  <section class="mdf">
    <div class="abs mdf-photo" role="img" aria-label="Close-up of light wood MDF panel surface"></div>
    <span class="dot"></span>
    <p class="abs eyebrow">MDF products</p>
    <h2 class="abs h2">MDF panels available alongside packaging supply.</h2>
    <p class="abs body-s">While the website direction keeps the main look packaging-focused, Brixel can also present MDF panels as a secondary product line with a clean, professional section.</p>
    <ul class="ticks">
      <li><svg width="8" height="8" viewBox="0 0 8 8"><path d="M1 4.2l2 2L7 1.8" fill="none" stroke="#1ea7f5" stroke-width="1.4"/></svg>Commercial supply support</li>
      <li><svg width="8" height="8" viewBox="0 0 8 8"><path d="M1 4.2l2 2L7 1.8" fill="none" stroke="#1ea7f5" stroke-width="1.4"/></svg>Custom sourcing options</li>
      <li><svg width="8" height="8" viewBox="0 0 8 8"><path d="M1 4.2l2 2L7 1.8" fill="none" stroke="#1ea7f5" stroke-width="1.4"/></svg>Simple request-a-quote workflow</li>
    </ul>
  </section>

  <section class="cta">
    <h2>Need a custom packaging solution?</h2>
    <p>Send your product details, size, material preference and order goals. Brixel will help source the right option.</p>
    <a href="#">Start a Quote</a>
  </section>

  <section class="contact">
    <span class="dot"></span>
    <p class="abs eyebrow">Contact</p>
    <h2 class="abs h2">Let’s build the right packaging program.</h2>
    <p class="abs details">Owner: Dana Whitfield<br>Mobile: 555-014-2278<br>Email: Dana.Whitfield@Brix-El.com</p>

    <div class="field" style="left:475px;top:52px;width:178px">Name</div>
    <div class="field" style="left:660px;top:52px;width:178px">Email</div>
    <div class="field" style="left:475px;top:92px;width:178px">Company</div>
    <div class="field select" style="left:660px;top:92px;width:178px"><span>Product Interest</span><svg width="7" height="5" viewBox="0 0 7 5"><path d="M1 1l2.5 2.5L6 1" fill="none" stroke="#0f1a33" stroke-width="1"/></svg></div>
    <div class="field area" style="left:475px;top:132px;width:363px">Tell us about your packaging needs</div>
    <span class="submit">Submit Request</span>
  </section>

  <footer>
    <div class="foot-brand"><span class="brand-mark"></span><span>Brixel Solutions</span></div>
    <p class="foot-copy">© 2026 Brixel Solutions. Custom flexible packaging, safety supplies, strapping, stretch film and MDF products.</p>
  </footer>

</div>
</body>
</html>
```